Harborline Stay Collective Business Card Design

Design a business card for Harborline Stay Collective. Look at the website for colors and reference. Card should have logo, name, title, office number, mobile number, email, URL and a tagline like, "Luxury Hotel & Resort Email Marketing" (This might change).

https://www.harborlinestaycollective.net

The rest I will leave up to your imagination.

Contact Information for Business Card

Logo, name, title, office number, mobile number, email, URL and a tagline like, "Luxury Hotel & Resort Email Marketing" (This might change).

```html
<!DOCTYPE html>
<html lang="en">
<head>
<meta charset="utf-8">
<title>Harborline Stay Collective – Business Card</title>
<link href="https://fonts.googleapis.com/css2?family=Montserrat:wght@400;500;600&display=swap" rel="stylesheet">
<style>
  :root {
    --backdrop: #141415;
    --card: #1e1e1f;
    --accent: #ec7320;
    --text-light: #e6e6e6;
    --logo-grey: #bdbdbd;
  }
  * { margin: 0; padding: 0; box-sizing: border-box; }
  html, body {
    width: 900px;
    height: 1200px;
    overflow: hidden;
    background: var(--backdrop);
    font-family: "Montserrat", Arial, sans-serif;
  }
  .canvas {
    position: relative;
    width: 900px;
    height: 1200px;
  }
  .card {
    position: absolute;
    left: 135px;
    width: 630px;
    height: 357px;
    background: var(--card);
  }
  .card--front { top: 215px; }
  .card--back { top: 628px; }

  /* Front */
  .brand {
    position: absolute;
    left: 0;
    right: 0;
    top: 164px;
    display: flex;
    align-items: center;
    justify-content: center;
    gap: 12px;
  }
  .brand__square {
    width: 14px;
    height: 14px;
    background: var(--accent);
  }
  .brand__name {
    font-weight: 600;
    font-size: 22px;
    letter-spacing: 3px;
    color: var(--logo-grey);
    text-transform: uppercase;
  }

  /* Back */
  .frame {
    position: absolute;
    left: 39px;
    top: 33px;
    width: 552px;
    height: 292px;
    border: 3px solid var(--accent);
  }
  .contact {
    position: absolute;
    left: 0;
    right: 0;
    text-align: center;
    color: var(--text-light);
  }
  .contact__name {
    top: 84px;
    font-weight: 600;
    font-size: 24px;
    letter-spacing: 1px;
    color: var(--accent);
  }
  .contact__title {
    top: 119px;
    font-size: 17px;
    letter-spacing: 1px;
  }
  .contact__rule {
    position: absolute;
    left: 269px;
    top: 145px;
    width: 93px;
    height: 3px;
    background: var(--accent);
  }
  .contact__lines {
    top: 171px;
    font-size: 17px;
    line-height: 26px;
  }
  .contact__phone { letter-spacing: 3.5px; }
  .contact__web { letter-spacing: 1px; font-size: 16.5px; }
  .tagline {
    position: absolute;
    left: 0;
    right: 0;
    top: 313px;
    text-align: center;
  }
  .tagline span {
    display: inline-block;
    padding: 0 11px;
    background: var(--card);
    font-weight: 500;
    font-size: 14px;
    letter-spacing: 0.5px;
    color: var(--text-light);
    line-height: 20px;
  }
</style>
</head>
<body>
<main class="canvas">
  <section class="card card--front">
    <div class="brand">
      <span class="brand__square"></span>
      <span class="brand__name">Harborline Stay Collective</span>
    </div>
  </section>

  <section class="card card--back">
    <div class="frame"></div>
    <p class="contact contact__name">DANA WHITCOMBE</p>
    <p class="contact contact__title">President</p>
    <div class="contact__rule"></div>
    <div class="contact contact__lines">
      <p class="contact__phone">808.555.0142</p>
      <p class="contact__phone">561.555.0190</p>
      <p class="contact__web">info@harborlinestaycollective.net</p>
      <p class="contact__web">www.harborlinestaycollective.net</p>
    </div>
    <p class="tagline"><span>Luxury Hotel &amp; Resort Email Marketing</span></p>
  </section>
</main>
</body>
</html>
```